Site re-branding and modernization

Two Managed Service Providers (Information Technology) have merged and need an update to their website. The site needs to be re-branded from "Harbor Crest" with a blue theme to "Pinewell Systems" with an orange theme.

Pinewell Systems provides small and medium business with an outsourced IT department, offering enterprise level IT to business that otherwise wouldn't have it. Our marketing has been centered around a row of apples with one orange and a caption that says, "We work quietly and we're fine with that!" Hence the orange color scheme needed as well as a site that stands out from the typical MSP site.

We would like to maintain our current site in order to retain SEO, update the technology used (current site is flash based), mobile (iPhone, iPad, Windows Phone) compatible and Color Theme update (likely orange and white).

My current site:
http://www.pinewellsystems.net

My chief local competition (who we want to look better than):
http://www.lanternrelay.com/

Other MSP sites (people we want to stand out from):
http://www.ferngatehq.com/
http://www.quillmarsh.com/
Updates

Please send your email to rwhitby@pinewellnx.com if you are interested in this project so I can send you a dropbox link to the existing site files for you to work with.

https://www.filecove.example/sh/4k2pq8wzrtn51ab/QQX9LmcaTe3VbnoqsKdPW71y

We would like to have a Call to action form on the main page and an informational Video. In addition we would like the following Categories and coorisponding Icons on the Main Page. We will also need a page for each Sub-Category. The Tag line on the Landing Page / Banner should read "Managed IT for Growing Teams" Managed IT >Law Firms .>Associations / Nonprofits > Financial Services > Healthcare >Education Cloud Services >Server > Desktop >Managed Wireless > Voice > Restaurant Point of Sale >Brindle Suite 360 Migrations Data Center > Managed Servers > Managed Desktops >Disaster Recovery Hosting Professional Services >Virtualization >Backup & DR Planning >Vellum Switchworks >Mobile or Virtual Office Solutions

Target Market(s)

Small and medium business that want to have the best possible IT support.

Industry/Entity Type

Marketing

Colors
f37022

Requirements
Must have
• Convert Site from Flash to Latest web design technology i.e. DHTML. Site must be mobile friendly. Convert all Harbor Crest Logo Marks to Pinewell Systems Logo. Change Color Theme to match uploaded files.

```html
<!DOCTYPE html>
<html lang="en">
<head>
<meta charset="utf-8">
<title>Pinewell Systems — Home</title>
<link rel="stylesheet" href="https://fonts.googleapis.com/css2?family=Bowlby+One&family=PT+Sans:wght@400;700&display=swap">
<style>
  :root{
    --stage:#e6e6e6;
    --header:#2a2828;
    --header-edge:#3a3737;
    --orange:#f37022;
    --orange-pale:#fbd2b6;
    --white:#ffffff;
    --ink:#3b3b3b;
    --muted:#8a8a8a;
    --nav:#e9e9e9;
    --sky:#a9c6e2;
    --glass:#5d7f9e;
    --steel:#cfd4d8;
  }
  *{box-sizing:border-box;margin:0;padding:0}
  html,body{width:1200px;height:1200px;overflow:hidden;background:var(--stage)}
  body{font-family:"PT Sans",Arial,sans-serif;position:relative}

  .site{position:absolute;left:0;top:220px;width:1200px;height:760px;background:var(--white);overflow:hidden}

  /* header */
  .site-header{position:absolute;left:0;top:0;width:1200px;height:100px;background:var(--header);border-bottom:1px solid var(--header-edge)}
  .call-line{position:absolute;left:282px;top:10px;font-size:11px;color:#6c6868;letter-spacing:.3px}
  .brand{position:absolute;left:240px;top:34px;display:flex;align-items:center;gap:10px}
  .brand-mark{width:30px;height:30px;background:var(--orange);flex:none}
  .brand-text{display:flex;flex-direction:column}
  .brand-name{font-size:21px;font-weight:400;color:var(--nav);letter-spacing:1px;line-height:1;text-transform:uppercase}
  .brand-tagline{font-size:8px;font-weight:400;color:var(--nav);letter-spacing:.6px;margin-top:4px;text-transform:uppercase}
  .main-nav{position:absolute;left:634px;top:50px;display:flex;gap:26px}
  .main-nav a{font-size:13px;color:var(--nav);text-decoration:none;padding-bottom:5px}
  .main-nav a.is-current{color:var(--orange);border-bottom:2px solid var(--orange);font-weight:700}
  .social-strip{position:absolute;left:850px;top:12px;width:170px;height:30px}
  .social-strip svg{display:block}
  .social-strip .dots{position:absolute;left:30px;top:6px;display:flex;gap:18px}
  .social-strip .dots span{width:10px;height:10px;border-radius:50%;background:#bdbdbd}

  /* hero */
  .hero{position:absolute;left:0;top:100px;width:1200px;height:380px}
  .hero-art{position:absolute;left:0;top:0;display:block}
  .hero-copy{position:absolute;left:190px;top:90px;width:310px;text-align:center;color:var(--white)}
  .hero-title{font-family:"Bowlby One",Impact,sans-serif;font-size:40px;line-height:1;letter-spacing:1px}
  .hero-sub{font-size:24px;line-height:1.1;margin-top:4px}
  .hero-body{font-size:12px;line-height:1.35;margin-top:8px}
  .hero-button{display:inline-block;margin-top:16px;padding:6px 16px;background:var(--orange-pale);color:var(--ink);font-size:16px;border-radius:2px}
  .slide-arrow{position:absolute;top:90px;width:28px;height:34px;background:#1f1f1f;display:flex;align-items:center;justify-content:center}
  .slide-arrow svg{display:block}
  .slide-arrow.prev{left:0;background:#5a5a5a}
  .slide-arrow.next{right:0;top:140px}

  /* feature cards */
  .features{position:absolute;left:175px;top:440px;width:850px;height:220px;background:var(--white);border-radius:6px 6px 0 0;display:flex;gap:14px;padding:12px 14px}
  .feature{flex:1;display:flex;flex-direction:column;align-items:center}
  .feature-media{width:100%;height:118px}
  .feature-title{font-size:13px;font-weight:700;color:var(--ink);margin-top:10px}
  .feature-note{font-size:12px;color:var(--muted);margin-top:2px}
  .testimonials{width:100%;height:118px;background:#f4f4f4;padding:6px;display:flex;flex-direction:column;gap:6px}
  .quote{display:flex;gap:6px}
  .quote-portrait{width:30px;height:34px;flex:none;background:#b7aea6}
  .quote p{font-size:7.5px;line-height:1.3;color:#777}
  .quote cite{display:block;font-style:normal;font-size:7px;color:var(--orange);margin-top:2px}
</style>
</head>
<body>
<main class="site">
  <header class="site-header">
    <div class="call-line">Call today (555) 270-0100</div>
    <div class="brand">
      <span class="brand-mark"></span>
      <div class="brand-text">
        <span class="brand-name">Pinewell Systems.net</span>
        <span class="brand-tagline">Managed IT for Growing Teams</span>
      </div>
    </div>
    <div class="social-strip">
      <svg width="170" height="30" viewBox="0 0 170 30"><path d="M0 27 H150 L168 4" fill="none" stroke="var(--orange)" stroke-width="2"/></svg>
      <div class="dots"><span></span><span></span><span></span><span></span><span></span></div>
    </div>
    <nav class="main-nav">
      <a class="is-current" href="#">Home</a>
      <a href="#">IT Services</a>
      <a href="#">Internet Marketing</a>
      <a href="#">About</a>
      <a href="#">Contact us</a>
    </nav>
  </header>

  <section class="hero">
    <svg class="hero-art" width="1200" height="380" viewBox="0 0 1200 380">
      <defs>
        <linearGradient id="orangeField" x1="0" y1="0" x2="1" y2="0">
          <stop offset="0" stop-color="#f59a63"/>
          <stop offset="1" stop-color="#f37022"/>
        </linearGradient>
        <linearGradient id="skyline" x1="0" y1="0" x2="0" y2="1">
          <stop offset="0" stop-color="#a9c6e2"/>
          <stop offset=".55" stop-color="#5d7f9e"/>
          <stop offset="1" stop-color="#cfd4d8"/>
        </linearGradient>
      </defs>
      <rect width="1200" height="380" fill="url(#orangeField)" role="img" aria-label="Faded city skyline in orange tones"/>
      <polygon points="735,0 1200,0 1200,380 350,380" fill="url(#skyline)" role="img" aria-label="Glass office towers with rows of server racks"/>
      <polygon points="1200,250 1200,380 980,380" fill="#f37022"/>
      <polyline points="0,380 0,372 12,364 24,372 36,364 48,372 60,364 72,372 84,364 96,372 108,364 120,372 132,364 144,372 156,364 168,372 180,364 180,380" fill="#ffffff"/>
      <polyline points="1020,380 1020,364 1032,372 1044,364 1056,372 1068,364 1080,372 1092,364 1104,372 1116,364 1128,372 1140,364 1152,372 1164,364 1176,372 1188,364 1200,372 1200,380" fill="#ffffff"/>
    </svg>
    <div class="hero-copy">
      <div class="hero-title">PROACTIVE</div>
      <div class="hero-sub">Service Plans</div>
      <p class="hero-body">Being proactive, instead of reactive, is going to avoid unwanted "down time". Get started with one of our Service Plans today.</p>
      <span class="hero-button">Learn more</span>
    </div>
    <div class="slide-arrow prev"><svg width="10" height="14" viewBox="0 0 10 14"><path d="M8 1 L2 7 L8 13" fill="none" stroke="#fff" stroke-width="2"/></svg></div>
    <div class="slide-arrow next"><svg width="10" height="14" viewBox="0 0 10 14"><path d="M2 1 L8 7 L2 13" fill="none" stroke="#fff" stroke-width="2"/></svg></div>
  </section>

  <section class="features">
    <article class="feature">
      <div class="feature-media" role="img" aria-label="Hands at a desk with a search icon" style="background:linear-gradient(135deg,#d9d6d2,#f2f1ef)"></div>
      <h3 class="feature-title">Technology Answers</h3>
      <p class="feature-note">for you business</p>
    </article>
    <article class="feature">
      <div class="feature-media" role="img" aria-label="Person pointing at a computer monitor" style="background:linear-gradient(135deg,#e8e8e8,#b9bcc0)"></div>
      <h3 class="feature-title">I am looking for an</h3>
      <p class="feature-note">internet marketing solution</p>
    </article>
    <article class="feature">
      <div class="feature-media" role="img" aria-label="Business team shaking hands in an office" style="background:linear-gradient(135deg,#cdb8a6,#4a4a52)"></div>
      <h3 class="feature-title">I am interested</h3>
      <p class="feature-note">in outsourcing my I.T</p>
    </article>
    <article class="feature">
      <div class="testimonials">
        <div class="quote">
          <div class="quote-portrait" role="img" aria-label="Client portrait"></div>
          <p>Their team answered every call fast and fixed issues before we noticed.<cite>Dana Holt, Managing Partner</cite></p>
        </div>
        <div class="quote">
          <div class="quote-portrait" role="img" aria-label="Client portrait"></div>
          <p>Moving our servers to their care cut downtime and saved real money.</p>
        </div>
      </div>
      <h3 class="feature-title">Client Testimonials</h3>
      <p class="feature-note">Click here</p>
    </article>
  </section>
</main>
</body>
</html>
```